Tech Company Office Internal Feature Wall Ultra HighRes - Wall Paper Design

We need a graphic designer to come up with a cool design for an internal feature wall in our new office. Dimensions of the wall can be found in the PDF file “Interior Wall Dimensions.pdf”. We are a technology consultancy firm based in Perth, Western Australia that provides a number of IT services including datacentre/cloud services, software development, cyber security, managed services and more.

The vibe we are looking to go with is innovation, cutting edge, technology, cyber, revolutionary. When people see the feature wall it should scream “cutting edge” tech company.

With regards to the contents of the image, this is up to the designer however we would like to ask our logo to be featured on the wall somewhere (we uploaded two different logo samples of different layout in vector format).

As this will be printed large scale into wallpaper, the finished design must be extremely high resolution to ensure zero distorted pixilation during printing. We provided the dimensions of the wall under the PDF file “Interior Wall Dimensions.pdf”.

I have uploaded some photos of the wall (the desks/shelves in front of the wall will be moved).

I would love to see the designs that are uploaded.

```html
<!DOCTYPE html>
<html lang="en">
<head>
<meta charset="utf-8">
<title>Vantora Systems – Feature Wall</title>
<link href="https://fonts.googleapis.com/css2?family=Arimo:wght@400;700&family=Archivo+Black&display=swap" rel="stylesheet">
<style>
  :root {
    --navy-deep: #0a0c4f;
    --navy: #141c85;
    --navy-soft: #1c2896;
    --paper: #efeff1;
    --paper-shade: #e4e5ef;
    --ink: #1d2894;
    --band: #1a4cb0;
    --band-dark: #161f86;
    --white: #ffffff;
  }
  * { margin: 0; padding: 0; box-sizing: border-box; }
  html, body { width: 1200px; height: 393px; overflow: hidden; background: var(--paper); }
  .wall { position: relative; width: 1200px; height: 393px; overflow: hidden; font-family: "Arimo", Arial, sans-serif; }
  .panel { position: absolute; top: 0; height: 393px; overflow: hidden; }
  .panel--innovation { left: 0; width: 434px; background: var(--navy); }
  .panel--cloud { left: 434px; width: 254px; background: var(--paper); }
  .panel--revolution { left: 688px; width: 258px; background: linear-gradient(180deg, var(--navy-deep) 0%, var(--navy) 100%); }
  .panel--future { left: 946px; width: 254px; background: var(--paper); }
  .panel svg.band { position: absolute; inset: 0; }

  .texture { position: absolute; inset: 0; }
  .texture--dark { background: radial-gradient(ellipse at 55% 65%, var(--navy-soft) 0%, var(--navy-deep) 85%); }
  .texture--light { background: radial-gradient(ellipse at 40% 35%, var(--paper-shade) 0%, var(--paper) 75%); }

  .brand { position: absolute; left: 104px; top: 72px; display: flex; align-items: center; gap: 8px;
    color: var(--white); font-weight: 700; font-size: 15px; letter-spacing: 2px; text-transform: uppercase; }
  .brand__mark { width: 12px; height: 12px; background: var(--white); }

  .headline { position: absolute; font-size: 29.5px; font-weight: 400; white-space: nowrap; }
  .headline strong { font-family: "Archivo Black", Arial, sans-serif; font-weight: 400; font-size: 1.09em; }
  .headline--innovation { left: 102px; top: 163px; color: var(--white); line-height: 41px; }
  .headline--cloud { left: 478px; top: 56px; color: var(--ink); line-height: 37px; }
  .headline--future { left: 998px; top: 236px; color: var(--ink); line-height: 37px; }
</style>
</head>
<body>
<main class="wall">
  <section class="panel panel--innovation">
    <div class="texture texture--dark" role="img" aria-label="Decorative concentric ring pattern on deep navy"></div>
    <div class="brand"><span class="brand__mark"></span>Vantora Systems</div>
  </section>

  <section class="panel panel--cloud">
    <div class="texture texture--light" role="img" aria-label="Decorative scattered outline shapes on light grey"></div>
    <svg class="band" width="254" height="393" viewBox="0 0 254 393" fill="none">
      <defs>
        <linearGradient id="bandCloud" x1="0" y1="1" x2="1" y2="0">
          <stop offset="0" stop-color="var(--band)"/>
          <stop offset="1" stop-color="var(--band-dark)"/>
        </linearGradient>
      </defs>
      <path d="M20 393 C 80 300, 150 232, 254 222 L254 262 C 170 268, 110 320, 70 393 Z" fill="url(#bandCloud)"/>
    </svg>
  </section>
  <h2 class="headline headline--cloud">Building<br><strong>Cloud</strong> Native<br>Confidence</h2>

  <section class="panel panel--revolution">
    <svg class="band" width="258" height="393" viewBox="0 0 258 393" font-family="Arimo, Arial, sans-serif" font-size="31" fill="var(--white)">
      <text transform="translate(101 327) rotate(-90)">driving a</text>
      <text transform="translate(143 327) rotate(-90)">super <tspan font-family="Archivo Black, Arial, sans-serif" font-size="33">Revolution</tspan></text>
      <text transform="translate(185 327) rotate(-90)">of industry</text>
    </svg>
  </section>

  <section class="panel panel--future">
    <div class="texture texture--light" role="img" aria-label="Decorative rings and scattered outline shapes on light grey"></div>
    <svg class="band" width="254" height="393" viewBox="0 0 254 393" fill="none">
      <defs>
        <linearGradient id="bandFuture" x1="0" y1="0" x2="1" y2="0">
          <stop offset="0" stop-color="var(--band)"/>
          <stop offset="1" stop-color="var(--band-dark)"/>
        </linearGradient>
      </defs>
      <path d="M0 196 C 110 190, 190 150, 254 73 L254 131 C 190 200, 110 232, 0 235 Z" fill="url(#bandFuture)"/>
    </svg>
  </section>

  <h1 class="headline headline--innovation">Creating entirely<br>new worlds through<br><strong>Innovation</strong></h1>
  <h2 class="headline headline--future">Forming<br>new Future,<br><strong>Together.</strong></h2>
</main>
</body>
</html>
```